"Velvet Petal Hour" Fashion Show Invitation design

We need an invitation design for our fashion show with the theme "Velvet Petal Hour"

the design will be the cover of the invitation, save the date cards, program etc

We are a philanthropic organization. Would like to incorporate florals, jewel tones or pastels etc... not sure if theres a way O or need) to incorporate fashion into that in an elegant way.

Text should read The Carrowfield Circle Presents "Velvet Petal Hour"
Updates

I'm looking for the design/image for the cover of our invitation- The only text needed is The Carrowfield Circle Presents Velvet Petal Hour I'm looking for feminine, elegant, florals etc...

Font styles to use
Serif
Decorative
Script

Colors
b768aa
e667a6
85cae6

Requirements
Must have
• jewel tones or pastels, flowers,
Nice to have
• fashion?

```html
<!DOCTYPE html>
<html lang="en">
<head>
<meta charset="utf-8">
<title>Velvet Petal Hour – Fashion Show</title>
<link rel="stylesheet" href="https://fonts.googleapis.com/css2?family=Montserrat:wght@600&family=Pinyon+Script&family=Playfair+Display:wght@500&display=swap">
<style>
  :root {
    --ink: #0e1117;
    --gold: #c8aa7e;
    --gold-light: #e3caa0;
    --gold-deep: #8f714b;
    --petal-pink: #e48aa9;
    --petal-rose: #d86a8b;
    --petal-yellow: #f1dc8e;
    --leaf-green: #7fae84;
    --leaf-sage: #a8bf94;
  }
  html, body {
    margin: 0;
    padding: 0;
    width: 848px;
    height: 1200px;
    overflow: hidden;
    background: var(--ink);
  }
  .invitation {
    position: relative;
    width: 848px;
    height: 1200px;
    background: var(--ink);
    overflow: hidden;
  }
  .host {
    position: absolute;
    top: 196px;
    left: 0;
    width: 100%;
    margin: 0;
    text-align: center;
    font-family: "Montserrat", sans-serif;
    font-weight: 600;
    font-size: 21px;
    letter-spacing: 0.24em;
    color: var(--gold);
  }
  .presents {
    position: absolute;
    top: 248px;
    left: 0;
    width: 100%;
    margin: 0;
    text-align: center;
    font-family: "Pinyon Script", cursive;
    font-size: 44px;
    line-height: 1;
    color: var(--gold-light);
  }
  .floral-spray {
    position: absolute;
    border-radius: 50% 50% 40% 40% / 70% 70% 30% 30%;
  }
  .floral-spray--top {
    left: 131px;
    top: 423px;
    width: 616px;
    height: 101px;
    background: linear-gradient(90deg,
      var(--leaf-sage) 0%, var(--leaf-green) 18%, var(--petal-pink) 42%,
      var(--petal-rose) 58%, var(--leaf-sage) 72%, var(--leaf-green) 100%);
    opacity: 0.8;
  }
  .floral-spray--bottom {
    left: 213px;
    top: 854px;
    width: 406px;
    height: 88px;
    border-radius: 40% 40% 50% 50% / 30% 30% 70% 70%;
    background: linear-gradient(90deg,
      var(--leaf-green) 0%, var(--petal-yellow) 30%, var(--leaf-sage) 55%,
      var(--petal-pink) 100%);
    opacity: 0.8;
  }
  .title-frame {
    position: absolute;
    left: 114px;
    top: 524px;
    width: 630px;
    height: 330px;
    box-sizing: border-box;
    border: 2px solid var(--gold);
    background: var(--ink);
  }
  .title {
    position: absolute;
    left: 0;
    width: 100%;
    margin: 0;
    text-align: center;
    font-family: "Playfair Display", serif;
    font-weight: 500;
    color: var(--gold);
    text-shadow: 0 1px 0 var(--gold-deep);
    line-height: 1;
  }
  .title--upper {
    top: 43px;
    font-size: 64px;
    letter-spacing: 0.1em;
  }
  .title--main {
    top: 120px;
    font-size: 120px;
    letter-spacing: 0.02em;
  }
  .event-type {
    position: absolute;
    top: 262px;
    left: 0;
    width: 100%;
    margin: 0;
    text-align: center;
    font-family: "Playfair Display", serif;
    font-size: 26px;
    line-height: 1;
    letter-spacing: 0.42em;
    color: var(--gold);
  }
</style>
</head>
<body>
  <main class="invitation">
    <p class="host">THE CARROWFIELD CIRCLE</p>
    <p class="presents">Presents</p>

    <div class="floral-spray floral-spray--top" role="img" aria-label="Watercolour flower spray: pink tulips, small berries and green leaves rising above the title frame"></div>

    <div class="title-frame">
      <h1 class="title title--upper">VELVET PETAL</h1>
      <p class="title title--main">HOUR</p>
      <p class="event-type">FASHION SHOW</p>
    </div>

    <div class="floral-spray floral-spray--bottom" role="img" aria-label="Watercolour flower spray: yellow and pink blossoms, berries and green leaves hanging below the title frame"></div>
  </main>
</body>
</html>
```